New Quill Harbor Systems website Home Page (design only)

We are looking for a new design for our home page. Please access this url to see a mock-up for you to use
https://pelorabeats.example-sites.com/qhswebsite01. We would like the website to be "alive" so we are open to creative ideas for animated gifs and motion graphics but want to make sure that the overall feel and use of the movement communicates a high tech and innovative company. Please follow the Quillharbor brand guidelines attached. A good example of a website that we feel really meets the innovative feel with movement is https://k7.example/. Do not copy this website! We are providing it as a example for you.

```html
<!DOCTYPE html>
<html lang="en">
<head>
<meta charset="utf-8">
<title>Quill Harbor Systems — Home</title>
<link href="https://fonts.googleapis.com/css2?family=Poppins:wght@400;500;600;700&family=Roboto:wght@400;500;700&display=swap" rel="stylesheet">
<style>
:root{
  --bg:#040c1c;
  --panel:#0c1830;
  --green:#3d9a78;
  --green-light:#53b98a;
  --blue:#1f4fc0;
  --white:#ffffff;
  --muted:#c9d1de;
  --line:#2f5f55;
}
*{margin:0;padding:0;box-sizing:border-box}
html,body{width:1200px;height:5186px;overflow:hidden}
body{background:var(--bg);color:var(--white);font-family:'Roboto',Arial,sans-serif;position:relative}
.abs{position:absolute}
.heading{font-family:'Poppins',Arial,sans-serif;font-weight:700;font-size:38px;position:absolute;left:0;width:1200px;text-align:center;line-height:1}
.heading span{position:relative;display:inline-block}
.heading span::before{content:"";position:absolute;left:-26px;top:-18px;width:52px;height:52px;border-radius:50%;border:6px solid transparent;border-top-color:var(--blue);border-left-color:var(--green);transform:rotate(10deg)}
.lead{position:absolute;left:0;width:1200px;text-align:center;font-size:15px;line-height:26px;color:var(--white)}
.btn{position:absolute;background:var(--green);color:#fff;font-size:12px;font-weight:700;display:flex;align-items:center;justify-content:center;gap:8px;letter-spacing:.2px}
.btn .dot{width:11px;height:11px;border-radius:50%;background:#fff;display:inline-block;position:relative}
.btn .dot::after{content:"";position:absolute;left:3px;top:3px;border:3px solid transparent;border-left:4px solid var(--green);border-right:0}

/* header */
.site-header{top:0;left:0;width:1200px;height:97px}
.brand{display:flex;align-items:center;gap:12px}
.brand .mark{border-radius:50%;border:5px solid var(--white);flex:none}
.brand .name{display:flex;flex-direction:column;font-family:'Poppins',Arial,sans-serif;color:var(--white);line-height:1}
.brand .name b{font-weight:600}
.brand .name small{font-weight:400;color:var(--muted)}
.nav{top:40px;left:398px;font-size:13px;font-weight:700}
.nav a{color:var(--white);text-decoration:none;position:absolute;white-space:nowrap}
.nav a.active{color:var(--green-light)}

/* hero */
.hero-bg{top:97px;left:0;width:1200px;height:640px;background:radial-gradient(ellipse 70% 40% at 60% 58%,#1d3650 0%,#0c1a30 45%,var(--bg) 80%),var(--bg)}
.hero-title{top:194px;left:0;width:1200px;text-align:center;font-family:'Poppins',Arial,sans-serif;font-weight:700;font-size:44px}
.hero-sub{top:276px;left:0;width:1200px;text-align:center;font-size:24px;font-weight:500;color:var(--green-light)}
.hero-text{top:333px;left:0;width:1200px;text-align:center;font-size:17px;font-weight:700;line-height:32px}
.ticker{top:451px;left:211px;width:777px;height:64px;border:1px solid var(--line);background:rgba(4,12,28,.6);display:flex;align-items:center;font-size:13px;font-weight:700}
.ticker .badge{width:120px;height:92px;background:#f2f3f6;margin-left:28px;margin-top:-4px;flex:none}
.ticker .story{margin-left:34px;width:396px}
.ticker .sep{width:2px;height:26px;background:#fff;margin-right:40px}
.ticker .more{display:flex;align-items:center;gap:8px;font-size:12px}
.ticker .more i{width:11px;height:11px;border-radius:50%;background:#fff;display:inline-block}

/* solutions */
.ring-svg{position:absolute;width:214px;height:214px}
.sol-title{position:absolute;width:230px;text-align:center;font-size:15px;font-weight:700;top:1178px}
.sol-title::after{content:"";display:block;width:32px;height:2px;background:var(--green);margin:14px auto 0}
.sol-text{position:absolute;width:230px;top:1230px;font-size:13px;line-height:21px;text-align:justify;text-align-last:center;color:var(--muted)}

/* market */
.market-card{position:absolute;top:1637px;width:316px;height:258px;border-radius:14px 14px 0 0}
.market-label{position:absolute;top:1870px;width:202px;height:56px;background:var(--green);font-size:18px;font-weight:700;display:flex;align-items:center;justify-content:center}
.arrow-btn{position:absolute;top:1760px;width:40px;height:40px;border-radius:50%;display:flex;align-items:center;justify-content:center}

/* platforms */
.tab{position:absolute;top:2255px;height:50px;width:198px;border:1px solid #3b4a5e;font-size:13px;font-weight:500;color:var(--green-light);display:flex;align-items:center;justify-content:center}
.tab.active{background:var(--green);color:#fff;border-color:var(--green);font-size:15px;font-weight:700}
.plat-frame{top:2400px;left:126px;width:444px;height:374px;border:6px solid var(--green);border-top:0;border-left:0}
.plat-img{top:2385px;left:111px;width:450px;height:380px;background:linear-gradient(135deg,#1c4a78 0%,#0d2c55 40%,#0a2040 70%,#1a4d6e 100%)}
.plat-title{top:2374px;left:663px;font-family:'Poppins',Arial,sans-serif;font-size:30px;font-weight:700}
.plat-sub{top:2427px;left:663px;font-size:19px;font-weight:700;color:var(--green-light)}
.plat-list{top:2472px;left:663px;width:430px;list-style:none;font-size:13px;line-height:30px}
.plat-list li{padding-left:38px;position:relative}
.plat-list li::before{content:"";position:absolute;left:0;top:9px;width:12px;height:12px;border-radius:50%;background:var(--green)}
.plat-list li::after{content:"";position:absolute;left:3px;top:11px;width:5px;height:3px;border-left:2px solid #fff;border-bottom:2px solid #fff;transform:rotate(-45deg)}

/* customers */
.cust-wave{top:3280px;left:0;width:1200px;height:240px;background:radial-gradient(ellipse 60% 50% at 50% 60%,#14263f 0%,transparent 70%)}
.cust-grid{top:3140px;left:111px;width:978px;display:grid;grid-template-columns:repeat(5,187px);gap:20px 10px}
.cust{height:101px;background:var(--panel);border-radius:10px;display:flex;align-items:center;justify-content:center;font-size:20px;font-weight:700;color:#fff}

/* next step */
.step-title{position:absolute;top:3960px;width:340px;text-align:center;font-family:'Poppins',Arial,sans-serif;font-size:21px;font-weight:600}
.step-text{position:absolute;top:4024px;width:260px;text-align:center;font-size:12px;line-height:22px;color:var(--muted)}

/* news */
.news-img{position:absolute;top:4360px;width:314px;height:240px;border-radius:14px}
.news-date{position:absolute;top:4610px;font-size:17px;font-weight:700}
.news-text{position:absolute;top:4646px;width:280px;font-size:12.5px;line-height:22px;color:var(--muted)}

/* footer */
.foot-head{position:absolute;top:4852px;font-family:'Poppins',Arial,sans-serif;font-size:16px;font-weight:500;letter-spacing:1px;font-variant:small-caps}
.foot-links{position:absolute;top:4902px;left:582px;list-style:none;font-size:13px;line-height:30.2px}
.foot-links li{padding-left:24px;position:relative}
.foot-links li::before{content:"";position:absolute;left:0;top:13px;width:5px;height:5px;border-radius:50%;background:var(--green)}
.contact{position:absolute;left:795px;display:flex;gap:22px;align-items:flex-start}
.contact .lbl{font-size:11px;font-weight:700;color:#3f87e0}
.contact .val{font-size:16px;margin-top:2px}
.copyright{top:5123px;left:0;width:1200px;height:63px;background:var(--green);font-size:13px;text-align:center;line-height:46px}
</style>
</head>
<body>

<svg width="0" height="0" style="position:absolute">
  <defs>
    <radialGradient id="core" cx="50%" cy="40%" r="60%">
      <stop offset="0" stop-color="#2f6fe0"/>
      <stop offset="1" stop-color="#0d2b86"/>
    </radialGradient>
    <g id="ring">
      <circle cx="107" cy="107" r="100" fill="none" stroke="#3d9a78" stroke-width="9" stroke-dasharray="420 300" transform="rotate(150 107 107)"/>
      <circle cx="107" cy="107" r="100" fill="none" stroke="#1f4fc0" stroke-width="9" stroke-dasharray="200 520" transform="rotate(-20 107 107)"/>
      <circle cx="107" cy="107" r="88" fill="none" stroke="#0f3a66" stroke-width="4"/>
      <circle cx="107" cy="107" r="76" fill="url(#core)"/>
    </g>
  </defs>
</svg>

<!-- Header -->
<header class="site-header abs">
  <div class="brand abs" style="left:111px;top:16px">
    <span class="mark" style="width:62px;height:62px"></span>
    <span class="name"><b style="font-size:21px">Quill Harbor</b><small style="font-size:12px;margin-top:3px">Systems</small></span>
  </div>
  <nav class="nav abs">
    <a class="active" style="left:0">Home</a>
    <a style="left:65px">Solutions</a>
    <a style="left:154px">How it works</a>
    <a style="left:264px">Our Market</a>
    <a style="left:362px">Data Value</a>
    <a style="left:459px">More ▾</a>
  </nav>
  <div class="btn" style="left:944px;top:26px;width:143px;height:44px">BOOK DEMO
    <svg width="12" height="12" viewBox="0 0 12 12"><rect x="1" y="2" width="10" height="9" fill="none" stroke="#fff" stroke-width="1.5"/><line x1="1" y1="5" x2="11" y2="5" stroke="#fff" stroke-width="1.5"/></svg>
  </div>
</header>

<!-- Hero -->
<div class="hero-bg abs" role="img" aria-label="Glowing particle network wave across a dark background"></div>
<h1 class="hero-title abs">Your Data Connection To Web 3.0</h1>
<p class="hero-sub abs">Are you ready to joining the global data economy?</p>
<p class="hero-text abs">Quillharbor's patented SaaS platform transforms your data into crypto tokens to trade on our<br>Insight Data Exchange</p>
<div class="ticker abs">
  <div class="badge" role="img" aria-label="League badge"></div>
  <div class="story">After hurricane, Hallberg fundraising for hometown</div>
  <div class="sep"></div>
  <div class="more">LEARN MORE <i></i></div>
</div>

<!-- Solutions -->
<h2 class="heading" style="top:786px"><span>Solutions</span></h2>
<p class="lead" style="top:853px">Quill Harbor Systems provides a number of solutions for your business, from a marketplace to trade data to a cutting<br>edge method of increasing customer engagements.</p>

<svg class="ring-svg" style="left:108px;top:934px" viewBox="0 0 214 214"><use href="#ring"/>
  <path d="M72 86h22l6 7h42v42H72z" fill="#fff"/><path d="M80 78h20l6 7h40v42" fill="none" stroke="#fff" stroke-width="4"/></svg>
<svg class="ring-svg" style="left:364px;top:934px" viewBox="0 0 214 214"><use href="#ring"/>
  <rect x="67" y="72" width="80" height="66" rx="6" fill="#fff"/><rect x="72" y="86" width="70" height="46" fill="#1f4fc0"/>
  <rect x="92" y="110" width="6" height="18" fill="#fff"/><rect x="102" y="102" width="6" height="26" fill="#fff"/><rect x="112" y="114" width="6" height="14" fill="#fff"/><rect x="122" y="106" width="6" height="22" fill="#fff"/></svg>
<svg class="ring-svg" style="left:622px;top:934px" viewBox="0 0 214 214"><use href="#ring"/>
  <rect x="96" y="66" width="52" height="70" rx="4" fill="#fff"/><path d="M74 92h16v14l14 26H60l14-26z" fill="#fff" stroke="#1f4fc0" stroke-width="3"/><circle cx="134" cy="120" r="12" fill="#1f4fc0" stroke="#fff" stroke-width="3"/></svg>
<svg class="ring-svg" style="left:877px;top:934px" viewBox="0 0 214 214"><use href="#ring"/>
  <ellipse cx="107" cy="80" rx="32" ry="10" fill="#fff"/><path d="M75 88v12c0 6 14 10 32 10s32-4 32-10V88c0 6-14 10-32 10s-32-4-32-10z" fill="#fff"/><path d="M75 108v12c0 6 14 10 32 10s32-4 32-10v-12c0 6-14 10-32 10s-32-4-32-10z" fill="#fff"/></svg>

<div class="sol-title" style="left:100px">Insight Data Exchange</div>
<div class="sol-title" style="left:356px">Quillharbor NFT</div>
<div class="sol-title" style="left:614px">Data Share</div>
<div class="sol-title" style="left:869px">Aurio</div>
<p class="sol-text" style="left:100px">Our Insight Data Exchange is a multifunctional, patented, data exchange platform empowering users with the knowledge</p>
<p class="sol-text" style="left:356px">Quillharbor NFT standardizes pricing by making every token and data type interchangeable with any other, regardless of its source.</p>
<p class="sol-text" style="left:614px">The Data Share platform provides non-profit organizations and businesses the ability to donate unused data</p>
<p class="sol-text" style="left:869px">The Aurio platform delivers individualized content that immediate increases engagement over any communication</p>

<!-- Market -->
<h2 class="heading" style="top:1479px"><span>Our Market</span></h2>
<p class="lead" style="top:1547px">Your data is a form of capital that can be monetized as a new revenue stream, mined for business insights,<br>or used to generate new products and services.</p>
<div class="arrow-btn" style="left:32px;background:#fff"><svg width="14" height="14" viewBox="0 0 14 14"><path d="M9 2L4 7l5 5" fill="none" stroke="#0c1830" stroke-width="2"/></svg></div>
<div class="arrow-btn" style="left:1126px;background:#1f4fc0"><svg width="14" height="14" viewBox="0 0 14 14"><path d="M5 2l5 5-5 5" fill="none" stroke="#fff" stroke-width="2"/></svg></div>
<div class="market-card" style="left:111px;background:linear-gradient(160deg,#b9c7d8,#6f87a8 55%,#3c5578)" role="img" aria-label="Laboratory microscope in blue light"></div>
<div class="market-card" style="left:443px;background:linear-gradient(180deg,#b9c1c4,#5d7468 45%,#2f4a3c)" role="img" aria-label="Misty forest valley with a lake"></div>
<div class="market-card" style="left:775px;background:linear-gradient(180deg,#a88f63,#7a6240 50%,#3e3325)" role="img" aria-label="Person walking through a cornfield"></div>
<div class="market-label" style="left:167px">Biotech</div>
<div class="market-label" style="left:499px">Carbon Credits</div>
<div class="market-label" style="left:831px">Commodities</div>

<!-- Platforms -->
<h2 class="heading" style="top:2167px"><span>Quillharbor Plateforms</span></h2>
<div class="tab active" style="left:179px">Refinery</div>
<div class="tab" style="left:394px">Quillharbor</div>
<div class="tab" style="left:608px">Insight Data Exchange</div>
<div class="tab" style="left:822px">NFT Exchange</div>
<div class="plat-frame abs"></div>
<div class="plat-img abs" role="img" aria-label="Businessman's hand above a glowing rising stock chart"></div>
<h3 class="plat-title abs">Refinery</h3>
<p class="plat-sub abs">Make your data work for you.</p>
<ul class="plat-list abs">
  <li>Capture structured and unstructured data from different locations (audio, video, image, script).</li>
  <li>Transform data into standardized, saleable “objects” using machine learning and artificial intelligence.</li>
  <li>Retain 100% control over your data assets.</li>
  <li>Extract value of business intelligence.</li>
  <li>Use AI-driven insights to uncover hidden value and develop new visualizations.</li>
</ul>
<div class="btn" style="left:664px;top:2738px;width:170px;height:42px">GO FOR REFINERY <span class="dot"></span></div>

<!-- Customers -->
<h2 class="heading" style="top:2972px"><span>Quillharbor Customers</span></h2>
<p class="lead" style="top:3039px;line-height:30px">By leveraging data, optimizing performance and constantly improving our data-delivery solutions, we help our clients<br>align their digital transformations with their core business and trading strategies.</p>
<div class="cust-wave abs" role="img" aria-label="Faint digital wave texture"></div>
<div class="cust-grid abs">
  <div class="cust">Aurio</div>
  <div class="cust">Lumora</div>
  <div class="cust">Corvane</div>
  <div class="cust">Echolens</div>
  <div class="cust">Stratwell</div>
  <div class="cust">Brightfold</div>
  <div class="cust">Paywise</div>
  <div class="cust">Minthaven</div>
  <div class="cust">Finlux</div>
  <div class="cust">Tradex</div>
</div>
<div class="btn" style="left:531px;top:3394px;width:137px;height:48px">VIEW ALL <span class="dot"></span></div>

<!-- Next step -->
<h2 class="heading" style="top:3615px"><span>Take the next step</span></h2>
<svg class="ring-svg" style="left:145px;top:3710px" viewBox="0 0 214 214">
  <circle cx="107" cy="107" r="100" fill="none" stroke="#1f4fc0" stroke-width="14"/><circle cx="107" cy="107" r="84" fill="#0b1a3a"/>
  <path d="M107 60l10 9 13-2 3 13 12 7-6 12 6 12-12 7-3 13-13-2-10 9-10-9-13 2-3-13-12-7 6-12-6-12 12-7 3-13 13 2z" fill="#fff"/>
  <circle cx="96" cy="96" r="7" fill="#0b1a3a"/><circle cx="118" cy="118" r="7" fill="#0b1a3a"/><line x1="120" y1="92" x2="94" y2="122" stroke="#0b1a3a" stroke-width="5"/></svg>
<svg class="ring-svg" style="left:493px;top:3710px" viewBox="0 0 214 214">
  <circle cx="107" cy="107" r="100" fill="none" stroke="#3d9a78" stroke-width="14"/><circle cx="107" cy="107" r="84" fill="#0b1a3a"/>
  <rect x="66" y="72" width="76" height="66" rx="6" fill="#fff"/><rect x="66" y="72" width="76" height="14" fill="#cfd6e4"/>
  <g fill="#0b1a3a"><rect x="74" y="94" width="9" height="8"/><rect x="89" y="94" width="9" height="8"/><rect x="104" y="94" width="9" height="8"/><rect x="74" y="108" width="9" height="8"/><rect x="89" y="108" width="9" height="8"/><rect x="74" y="122" width="9" height="8"/></g>
  <circle cx="136" cy="132" r="20" fill="#fff" stroke="#0b1a3a" stroke-width="4"/><path d="M136 120v12h9" fill="none" stroke="#0b1a3a" stroke-width="3"/></svg>
<svg class="ring-svg" style="left:839px;top:3710px" viewBox="0 0 214 214">
  <circle cx="107" cy="107" r="100" fill="none" stroke="#1f4fc0" stroke-width="14"/><circle cx="107" cy="107" r="84" fill="#0b1a3a"/>
  <rect x="74" y="64" width="54" height="84" rx="3" fill="#fff"/><rect x="134" y="72" width="12" height="56" fill="#fff"/><path d="M134 128h12l-6 12z" fill="#fff"/>
  <g stroke="#0b1a3a" stroke-width="4" fill="none"><path d="M80 80l4 4 6-7M80 100l4 4 6-7M80 120l4 4 6-7"/><path d="M96 82h24M96 102h24M96 122h24"/></g></svg>
<div class="step-title" style="left:82px">Contact Sales</div>
<div class="step-title" style="left:430px">Schedule A Demo</div>
<div class="step-title" style="left:776px">Request Information</div>
<p class="step-text" style="left:122px">Learn how our patented software platforms can help your organization.</p>
<p class="step-text" style="left:470px">See our solutions in action</p>
<p class="step-text" style="left:816px">For all other questions, please contact us here</p>

<!-- News -->
<h2 class="heading" style="top:4180px"><span>Quillharbor in the News</span></h2>
<p class="lead" style="top:4249px;line-height:29px">Whether you're a business in need of market data, a developer in the blockchain space, or simply<br>an individual who trades in NFTs - Quillharbor has a solution to fit your needs.</p>
<div class="news-img" style="left:111px;background:linear-gradient(135deg,#d8d4cc,#9a948a 55%,#4a4640)" role="img" aria-label="Exchange platform launch announcement with a classical building"></div>
<div class="news-img" style="left:447px;background:linear-gradient(180deg,#4aa7b0,#2e8a92 60%,#c9a24a)" role="img" aria-label="Yellow wildflowers against a teal sky"></div>
<div class="news-img" style="left:785px;background:linear-gradient(135deg,#d9b52a,#b89214 60%,#6d5a12)" role="img" aria-label="Yellow door with a round porthole window"></div>
<div class="news-date" style="left:128px">October 12, 2022</div>
<div class="news-date" style="left:464px">I'm an image title</div>
<div class="news-date" style="left:802px">I'm an image title</div>
<p class="news-text" style="left:128px">Emerging Artists to be Launched Under Brand Name 'Tidewell'</p>
<p class="news-text" style="left:464px">Emerging Artists to be Launched Under Brand Name 'Tidewell'</p>
<p class="news-text" style="left:802px">Emerging Artists to be Launched Under Brand Name 'Tidewell'</p>

<!-- Footer -->
<footer>
  <div class="brand abs" style="left:137px;top:4912px;gap:18px">
    <span class="mark" style="width:100px;height:100px;border-width:7px"></span>
    <span class="name"><b style="font-size:34px">Quill Harbor</b><small style="font-size:17px;margin-top:6px">Systems</small></span>
  </div>
  <div class="foot-head" style="left:582px">Quick Links</div>
  <ul class="foot-links">
    <li>Home</li><li>Solutions</li><li>How it works</li><li>Our Market</li><li>Data Value</li><li>Companay</li><li>Contact</li>
  </ul>
  <div class="foot-head" style="left:795px">Contact Us</div>
  <div class="contact" style="top:4910px">
    <svg width="20" height="30" viewBox="0 0 20 30"><rect x="2" y="1" width="16" height="28" rx="3" fill="none" stroke="#fff" stroke-width="2"/><line x1="7" y1="25" x2="13" y2="25" stroke="#fff" stroke-width="2"/></svg>
    <div><div class="lbl">PHONE NO :</div><div class="val">+ 1 555 010 2040</div></div>
  </div>
  <div class="contact" style="top:4978px">
    <svg width="26" height="20" viewBox="0 0 26 20"><rect x="1" y="1" width="24" height="18" fill="none" stroke="#fff" stroke-width="2"/><path d="M1 1l12 10L25 1" fill="none" stroke="#fff" stroke-width="2"/></svg>
    <div><div class="lbl">E MAIL :</div><div class="val" style="font-size:14px">info@quillharbor.example</div></div>
  </div>
  <div class="contact" style="top:5040px">
    <svg width="26" height="20" viewBox="0 0 26 20"><rect x="1" y="1" width="24" height="18" fill="none" stroke="#fff" stroke-width="2"/><path d="M1 1l12 10L25 1" fill="none" stroke="#fff" stroke-width="2"/></svg>
    <div><div class="lbl">LOCATION :</div><div class="val" style="font-size:14px">147 , Lorem Ipsum Dolor , United States</div></div>
  </div>
  <div class="copyright abs">© 2022 Quillharbor. All Rights Reserved</div>
</footer>

</body>
</html>
```